Flyer-Design für KL Kurier
Zielgruppe
Wir transportieren Dokumente, Pakete, Sperrgut und Paletten weltweit per Luftfracht. Unsere Zielgruppe sind Firmenkunden bis 300 Mitarbeiter die internationalen Versand haben.
Aufgabenstellung
Der Flyer soll DIN A 5 sein, beide Seiten bedruckt. Der Kunde soll den Flyer an seine Schreibtischunterlage legen, an die Pinnwand heften, auf jeden Fall aufheben. Dazu können Sie auch eine Stanzform gestalten. Uns soll der Kunden anrufen, wenn er Probleme hat. Das kann sein: Die Laufzeit(Liefergeschwindigkeit) von seinem jetzigen Anbieter ist zu langsam oder sein jetziger Anbieter kann den Transport gar nicht durchführen. Also immer, wenn Probleme auftreten oder der Transport mehr als 300 Euro kostet, dann soll der Kunden uns anrufen. Wir sind quasi die Transportfeuerwehr und helfen, wenn es brennt. Das heißt, dass der Kunden uns nicht täglich nutzen. Das muss im Flyer klarwerden. „Ich hebe den Flyer auf und wenn es brennt, rufe ich bei KL Kurier an, die helfen mir weiter.“ Vielleicht integrieren Sie einen Feuermelder oder ähnliches.
Wir haben auch festgestellt, dass Kunden Flyer die gefalzt sind oder größer als A5 nicht aufheben.

```html
<!DOCTYPE html>
<html lang="de">
<head>
<meta charset="utf-8">
<title>KL Kurier – Flyer A5</title>
<link href="https://fonts.googleapis.com/css2?family=Roboto+Condensed:wght@400;700&family=Roboto:wght@300;400;500&display=swap" rel="stylesheet">
<style>
:root{
  --bg:#d9d9d9;
  --paper:#ffffff;
  --green:#6fb64a;
  --yellow:#f2e531;
  --red:#c4161c;
  --ink:#1d1d1b;
  --ink-soft:#333333;
  --fire-1:#5a1a08;
  --fire-2:#c9461a;
  --fire-3:#f3a03a;
}
*{box-sizing:border-box;margin:0;padding:0}
html,body{width:1200px;height:1200px;overflow:hidden;background:var(--bg)}
body{position:relative;font-family:"Roboto",Arial,sans-serif;color:var(--ink)}

.flyer{position:absolute;width:700px;height:495px;background:var(--paper);overflow:hidden;box-shadow:0 6px 18px rgba(0,0,0,.25)}
.flyer--front{left:60px;top:70px}
.flyer--back{left:440px;top:625px}

/* front */
.front__photo{position:absolute;left:0;top:0;width:700px;height:400px;
  background:radial-gradient(ellipse at 65% 45%,var(--fire-3) 0%,var(--fire-2) 45%,var(--fire-1) 100%)}
.front__fade{position:absolute;left:0;top:0;width:388px;height:495px;
  background:linear-gradient(180deg,rgba(255,255,255,0) 0%,rgba(255,255,255,0) 28%,rgba(255,255,255,.92) 52%,#fff 62%)}
.front__stripe{position:absolute;top:0;width:12px;height:495px;background:var(--green)}
.front__stripe--left{left:38px}
.front__stripe--mid{left:372px}
.front__band{position:absolute;left:384px;top:400px;width:316px;height:95px;background:var(--paper)}
.front__bottom-left{position:absolute;left:50px;top:430px;width:322px;height:65px;background:var(--paper)}
.headline{position:absolute;left:68px;top:112px;font-family:"Roboto Condensed",Arial,sans-serif;font-weight:700;
  font-size:38px;line-height:42px;color:#fff;text-shadow:2px 2px 0 var(--red),-1px -1px 0 var(--red),1px -1px 0 var(--red),-1px 1px 0 var(--red)}
.phone{position:absolute;left:68px;top:202px;font-family:"Roboto Condensed",Arial,sans-serif;font-weight:700;
  font-size:32px;color:#fff;text-shadow:2px 2px 0 var(--red),-1px -1px 0 var(--red),1px -1px 0 var(--red),-1px 1px 0 var(--red)}
.benefits{position:absolute;left:70px;top:282px;list-style:none;font-family:"Roboto Condensed",Arial,sans-serif;font-size:12.5px;color:var(--ink-soft)}
.benefits li{display:flex;align-items:center;gap:9px;height:27px}
.benefits svg{width:11px;height:11px;flex:none}
.brand{position:absolute;display:flex;align-items:center;gap:12px;font-family:"Roboto Condensed",Arial,sans-serif;font-weight:700;color:var(--ink)}
.brand__mark{width:34px;height:34px;background:var(--green)}
.brand--front{left:440px;top:418px;font-size:40px}

/* back */
.back__panel{position:absolute;left:55px;top:0;width:266px;height:495px;background:var(--green)}
.back__rule{position:absolute;top:0;width:10px;height:495px;background:var(--yellow)}
.back__rule--left{left:45px}
.back__rule--right{left:321px}
.address{position:absolute;left:90px;top:375px;color:#fff;font-family:"Roboto",Arial,sans-serif;font-style:normal;font-size:12px;line-height:17px;font-weight:300}
.address__name{font-family:"Roboto Condensed",Arial,sans-serif;font-weight:700;margin-bottom:6px}
.address__gap{height:8px}
.back__title{position:absolute;left:370px;top:100px;font-family:"Roboto Condensed",Arial,sans-serif;font-weight:700;font-size:25px;line-height:31px}
.cargo{position:absolute;left:370px;top:190px;list-style:none;font-family:"Roboto Condensed",Arial,sans-serif;font-weight:400;font-size:20px;letter-spacing:.5px}
.cargo li{display:flex;align-items:center;gap:10px;height:34px}
.cargo__dot{width:10px;height:10px;background:var(--green);flex:none}
.brand--back{left:390px;top:400px;font-size:40px}
</style>
</head>
<body>

<section class="flyer flyer--front" aria-label="Flyer Vorderseite">
  <div class="front__photo" role="img" aria-label="Foto: Feuerwehrmann in Schutzkleidung mit Atemschutz vor Flammen"></div>
  <div class="front__fade"></div>
  <div class="front__band"></div>
  <div class="front__bottom-left"></div>
  <div class="front__stripe front__stripe--left"></div>
  <div class="front__stripe front__stripe--mid"></div>

  <h1 class="headline">Wenn es brennt,<br>rufen Sie uns an!</h1>
  <p class="phone">0456/7890123</p>

  <ul class="benefits">
    <li><svg viewBox="0 0 12 12"><path d="M1 6.5l3 3L11 2" fill="none" stroke="var(--green)" stroke-width="2"/></svg>Wir helfen Ihnen bei Transportproblemen</li>
    <li><svg viewBox="0 0 12 12"><path d="M1 6.5l3 3L11 2" fill="none" stroke="var(--green)" stroke-width="2"/></svg>Heute abgeholt und heute noch zugestellt</li>
    <li><svg viewBox="0 0 12 12"><path d="M1 6.5l3 3L11 2" fill="none" stroke="var(--green)" stroke-width="2"/></svg>Zustellung in den USA am nächsten Tag</li>
    <li><svg viewBox="0 0 12 12"><path d="M1 6.5l3 3L11 2" fill="none" stroke="var(--green)" stroke-width="2"/></svg>Weltweiter Transport</li>
    <li><svg viewBox="0 0 12 12"><path d="M1 6.5l3 3L11 2" fill="none" stroke="var(--green)" stroke-width="2"/></svg>Erstellung Ihrer Exportpapiere</li>
    <li><svg viewBox="0 0 12 12"><path d="M1 6.5l3 3L11 2" fill="none" stroke="var(--green)" stroke-width="2"/></svg>Bester Kundendienst</li>
  </ul>

  <div class="brand brand--front"><span class="brand__mark"></span>KL Kurier</div>
</section>

<section class="flyer flyer--back" aria-label="Flyer Rückseite">
  <div class="back__panel"></div>
  <div class="back__rule back__rule--left"></div>
  <div class="back__rule back__rule--right"></div>

  <address class="address">
    <div class="address__name">KL Kurier</div>
    <div>Lindenweg 7</div>
    <div>12345 Beispielstadt</div>
    <div class="address__gap"></div>
    <div>post@kl-kurier.de</div>
    <div>Tel. 0456/7890123</div>
  </address>

  <h2 class="back__title">Weltweiter Transport<br>per Luftfracht</h2>
  <ul class="cargo">
    <li><span class="cargo__dot"></span>DOKUMENTE</li>
    <li><span class="cargo__dot"></span>PAKETE</li>
    <li><span class="cargo__dot"></span>SPERRGUT</li>
    <li><span class="cargo__dot"></span>PALETTEN</li>
  </ul>

  <div class="brand brand--back"><span class="brand__mark"></span>KL Kurier</div>
</section>

</body>
</html>
```